Insight Plus. needs Business Cards

For this project, we need business cards (currently have also put a call out for a logo). We are a start-up called Insight Plus. This is our second company (our first one was called Querivance). Traditionally we have been providing market research services across different sectors, primarily financial services and the pharmaceutical industry. However, we now want to go beyond market research to offer more (Plus.)... strategic consulting and big data knowledge management. We want our brand to be approachable, creative, fun but professional.

Target Market(s)

The target audience is a business professional - we are B2B (business to business) and do not sell our services to individuals. The brands we work with are major brands across industries, but primarily automotive, financial and pharmaceutical.

Industry/Entity Type

Market Research

Font styles to use
Serif
Sans Serif
Other font styles liked:
• Calibri

Requirements
Must have
• Be clean, simple, modern
Show our address and phone number and email address and website URL
We do not need to have titles showing.

```html
<!DOCTYPE html>
<html lang="en">
<head>
<meta charset="UTF-8">
<title>Insight Plus. Business Cards</title>
<link rel="stylesheet" href="https://fonts.googleapis.com/css2?family=Carlito:wght@400;700&display=swap">
<style>
  :root {
    --teal: #17b1a1;
    --teal-light: #7fd3cb;
    --backdrop: #3b3b3b;
    --white: #ffffff;
    --ink: #2b2b2b;
    --grey-mid: #9a9a9a;
    --grey-light: #cfcfcf;
    --black: #111111;
  }
  * { margin: 0; padding: 0; box-sizing: border-box; }
  html, body {
    width: 1200px;
    height: 750px;
    overflow: hidden;
    background: var(--backdrop);
    font-family: "Carlito", "Calibri", sans-serif;
  }
  .canvas {
    position: relative;
    width: 1200px;
    height: 750px;
  }
  .card {
    position: absolute;
    top: 211px;
    width: 512px;
    height: 292px;
    border-radius: 23px;
    overflow: hidden;
  }
  .card--back { left: 78px; background: var(--teal); }
  .card--front { left: 608px; background: var(--white); }

  .brand-name {
    position: absolute;
    color: var(--white);
    font-weight: 700;
    white-space: nowrap;
    letter-spacing: 0.2px;
  }
  .card--back .brand-name {
    right: 42px;
    bottom: 34px;
    font-size: 25px;
  }
  .front-band {
    position: absolute;
    left: 0; top: 39px;
    width: 100%; height: 89px;
    background: var(--teal);
  }
  .front-band .brand-name {
    left: 50%;
    top: 50%;
    transform: translate(-50%, -50%);
    font-size: 34px;
  }

  .colour-rule {
    position: absolute;
    top: 154px;
    height: 6px;
  }
  .colour-rule--teal { left: 25px; width: 187px; background: var(--teal); }
  .colour-rule--grey { left: 215px; width: 93px; background: var(--grey-mid); }
  .colour-rule--light { left: 311px; width: 80px; background: var(--grey-light); }
  .colour-rule--black { left: 393px; width: 88px; background: var(--black); }

  .contact-list {
    position: absolute;
    left: 26px;
    top: 174px;
    list-style: none;
    color: var(--ink);
    font-size: 15px;
    line-height: 17.5px;
  }
  .contact-list li {
    display: flex;
    align-items: center;
    gap: 12px;
  }
  .contact-icon { width: 12px; height: 12px; flex: none; }

  .address {
    position: absolute;
    right: 51px;
    top: 174px;
    text-align: right;
    color: var(--ink);
    font-size: 15px;
    line-height: 19px;
  }
  .address-pin {
    position: absolute;
    right: 31px;
    top: 177px;
    width: 12px;
    height: 14px;
  }
  .front-wave {
    position: absolute;
    left: 0; bottom: 0;
    width: 512px; height: 60px;
  }
</style>
</head>
<body>
<main class="canvas">
  <section class="card card--back" aria-label="Card back">
    <span class="brand-name">Insight Plus.</span>
  </section>

  <section class="card card--front" aria-label="Card front">
    <div class="front-band">
      <span class="brand-name">Insight Plus.</span>
    </div>

    <div class="colour-rule colour-rule--teal"></div>
    <div class="colour-rule colour-rule--grey"></div>
    <div class="colour-rule colour-rule--light"></div>
    <div class="colour-rule colour-rule--black"></div>

    <ul class="contact-list">
      <li>
        <svg class="contact-icon" viewBox="0 0 12 12" aria-hidden="true"><path fill="#17b1a1" d="M1 4c0-2 2-3 5-3s5 1 5 3v1H8.5V3.8h-5V5H1z M3 6h6l1.5 4h-9z"/></svg>
        <span>0123 456 789</span>
      </li>
      <li>
        <svg class="contact-icon" viewBox="0 0 12 12" aria-hidden="true"><rect x="2.5" y="0.8" width="7" height="10.4" rx="1" fill="none" stroke="#17b1a1" stroke-width="1.3"/></svg>
        <span>0123 456 789</span>
      </li>
      <li>
        <svg class="contact-icon" viewBox="0 0 12 12" aria-hidden="true"><rect x="1" y="2.5" width="10" height="7" fill="#17b1a1"/><path d="M1 2.5l5 4 5-4" fill="none" stroke="#fff" stroke-width="1"/></svg>
        <span>youremail@mail.com</span>
      </li>
      <li>
        <svg class="contact-icon" viewBox="0 0 12 12" aria-hidden="true"><g fill="none" stroke="#17b1a1" stroke-width="1"><circle cx="6" cy="6" r="4.8"/><ellipse cx="6" cy="6" rx="2" ry="4.8"/><path d="M1.2 6h9.6"/></g></svg>
        <span>www.yourwebsite.com</span>
      </li>
    </ul>

    <p class="address">address (street address<br>suite number, city, state, zip</p>
    <svg class="address-pin" viewBox="0 0 12 14" aria-hidden="true"><path fill="#2b2b2b" d="M6 0a5 5 0 0 0-5 5c0 3.5 5 9 5 9s5-5.5 5-9a5 5 0 0 0-5-5zm0 7a2 2 0 1 1 0-4 2 2 0 0 1 0 4z"/></svg>

    <svg class="front-wave" viewBox="0 0 512 60" preserveAspectRatio="none" aria-hidden="true">
      <path fill="#7fd3cb" d="M190 28 C300 40 420 30 512 5 L512 14 C420 40 300 46 190 28 Z"/>
      <path fill="#17b1a1" d="M0 32 C90 18 190 30 270 42 C360 54 440 44 512 24 L512 60 L0 60 Z"/>
    </svg>
  </section>
</main>
</body>
</html>
```